Business Advisory Firm Business Card

A clean, very upscale looking business card. Not crowded.

Please include logo (attached) and:

Daria K. Pellworth
Four Marlow Court
New York, NY 10023
tel: (917) 555-0143
fax: (646) 555-0172
email: dpellworth@quarrystoneconsultants.example
website: www.quarrystoneconsultants.example

Target Market(s)

Business clients. Often real estate development firms, other advisory firms or growing companies that need assistance. I would like a card that looks impressive and confident.

Industry/Entity Type

Business

Colors

Designer to choose colors to be used in the design.

Requirements
Must have
• Impressive and confident. Please include logo.
Should not have
• nothing flashy...

```html
<!DOCTYPE html>
<html lang="en">
<head>
<meta charset="utf-8">
<title>Quarrystone Advisory Services – Business Card</title>
<link href="https://fonts.googleapis.com/css2?family=Open+Sans:wght@400;600;700&display=swap" rel="stylesheet">
<style>
  :root {
    --backdrop: #2b1a12;
    --card-white: #ffffff;
    --green-dark: #6c7c12;
    --green-bright: #b2d00c;
    --green-text: #6a7a10;
    --ink: #222222;
    --ink-soft: #5e5e5e;
    --icon-green: #9cc21a;
    --ghost: #f3f4ee;
  }
  * { margin: 0; padding: 0; box-sizing: border-box; }
  html, body {
    width: 1200px; height: 1000px; overflow: hidden;
    background: var(--backdrop);
    font-family: "Open Sans", Arial, sans-serif;
  }
  .canvas { position: relative; width: 1200px; height: 1000px; }

  .card {
    position: absolute;
    box-shadow: 0 3px 8px rgba(0,0,0,0.45);
  }

  /* Back of card */
  .card-back {
    left: 119px; top: 141px; width: 554px; height: 324px;
    background: linear-gradient(90deg, var(--green-dark) 0%, #8fa912 28%, var(--green-bright) 47%, #9bb60f 65%, var(--green-dark) 100%);
  }
  .card-back .brand {
    position: absolute; left: 0; right: 0; top: 130px;
    display: flex; justify-content: center; align-items: center; gap: 10px;
    font-weight: 700; font-size: 22px; color: #ffffff;
  }
  .brand-square { width: 16px; height: 16px; background: #ffffff; }
  .card-back .web {
    position: absolute; left: 0; right: 0; top: 291px;
    text-align: center; color: #ffffff; font-size: 14px;
  }

  /* Front of card */
  .card-front {
    left: 473px; top: 541px; width: 618px; height: 360px;
    background: var(--card-white); overflow: hidden;
  }
  .card-front .brand {
    position: absolute; left: 30px; top: 40px;
    display: flex; align-items: flex-start; gap: 14px;
  }
  .card-front .brand-square { width: 28px; height: 28px; background: var(--icon-green); margin-top: 4px; }
  .brand-name {
    font-weight: 700; font-size: 22px; line-height: 26px; color: var(--ink);
  }
  .ghost-block {
    position: absolute; left: 395px; top: 190px; width: 240px; height: 190px;
    background: var(--ghost);
  }
  .holder { position: absolute; left: 439px; top: 142px; }
  .holder-name { font-weight: 700; font-size: 16px; color: var(--green-text); line-height: 22px; }
  .holder-title { font-size: 15px; color: var(--ink-soft); line-height: 22px; }

  .address {
    position: absolute; left: 16px; top: 192px;
    font-size: 16px; line-height: 22px; color: var(--ink);
  }
  .contacts { position: absolute; left: 15px; top: 247px; list-style: none; }
  .contacts li {
    display: flex; align-items: center; gap: 14px;
    height: 27px; font-size: 16px; color: var(--ink);
  }
  .contacts svg { width: 14px; height: 14px; flex: none; }
</style>
</head>
<body>
<div class="canvas">

  <section class="card card-back" aria-label="Card back">
    <div class="brand">
      <span class="brand-square"></span>
      <span>Quarrystone Advisory Services, Inc.</span>
    </div>
    <p class="web">www.quarrystoneconsultants.example</p>
  </section>

  <section class="card card-front" aria-label="Card front">
    <div class="ghost-block"></div>

    <div class="brand">
      <span class="brand-square"></span>
      <p class="brand-name">Quarrystone<br>Advisory<br>Services, Inc.</p>
    </div>

    <div class="holder">
      <p class="holder-name">Daria K. Pellworth</p>
      <p class="holder-title">CEO</p>
    </div>

    <p class="address">Four Marlow Court<br>New York, NY 10023</p>

    <ul class="contacts">
      <li>
        <svg viewBox="0 0 14 14" aria-label="Telephone"><rect x="2" y="1" width="9" height="12" rx="1" fill="var(--icon-green)"/><rect x="4" y="3" width="5" height="3" fill="#fff"/></svg>
        (917) 555-0143
      </li>
      <li>
        <svg viewBox="0 0 14 14" aria-label="Fax"><rect x="1" y="5" width="12" height="8" fill="var(--icon-green)"/><rect x="3" y="1" width="8" height="5" fill="var(--icon-green)"/><rect x="3" y="8" width="8" height="1.5" fill="#fff"/></svg>
        (646) 555-0172
      </li>
      <li>
        <svg viewBox="0 0 14 14" aria-label="Email"><rect x="1" y="3" width="12" height="8" fill="var(--icon-green)"/><path d="M1 3 L7 8 L13 3" stroke="#fff" stroke-width="1.2" fill="none"/></svg>
        dpellworth@quarrystoneconsultants.example
      </li>
      <li>
        <svg viewBox="0 0 14 14" aria-label="Website"><circle cx="7" cy="7" r="6" fill="var(--icon-green)"/><path d="M1 7 H13 M7 1 C4 4 4 10 7 13 M7 1 C10 4 10 10 7 13" stroke="#fff" stroke-width="0.9" fill="none"/></svg>
        www.quarrystoneconsultants.example
      </li>
    </ul>
  </section>

</div>
</body>
</html>
```